Real Estate Investment Company Needs A Business Card Designed

I need a business card designed for my use. We are a real estate investment company based in Omaha, Nebraska that specializes in buying, rehabbing and selling single family and multifamily properties. Would love designs that incorporate our logo and colors

Industry/Entity Type

Business

Contact Information for Business Card

Mitchell Parkhurst | President & CEO
4873 North 52nd Avenue, Ste 700
Omaha, NE 68142
(402) 786-4259
mitchell@kestrelgateproperties.example
www.KestrelgateProperties.example

Font styles to use
Serif

Colors
0255a3
3276b5

Requirements
Must have
• Our logo

```html
<!DOCTYPE html>
<html lang="en">
<head>
<meta charset="utf-8">
<title>Kestrelgate Business Card</title>
<link href="https://fonts.googleapis.com/css2?family=Work+Sans:wght@400;500;600&family=Roboto:wght@500&display=swap" rel="stylesheet">
<style>
  :root {
    --backdrop: #3b3c3d;
    --card-white: #ffffff;
    --card-dark: #1c1d1d;
    --brand-blue: #1a6fc1;
    --brand-blue-light: #5b9ad6;
    --silver-light: #e6e6e6;
    --silver-dark: #a9a9a9;
    --ink: #1f1f1f;
  }
  html, body {
    margin: 0;
    padding: 0;
    width: 1200px;
    height: 852px;
    overflow: hidden;
    background: var(--backdrop);
  }
  .canvas {
    position: relative;
    width: 1200px;
    height: 852px;
  }
  .card {
    position: absolute;
    top: 287px;
    width: 542px;
    height: 310px;
    border-radius: 14px;
    overflow: hidden;
    box-shadow: 0 6px 18px rgba(0,0,0,0.35);
  }
  .card-front { left: 46px; background: var(--card-white); }
  .card-back { left: 603px; background: var(--card-dark); }

  .edge-emblem {
    position: absolute;
    top: 60px;
    width: 244px;
    height: 244px;
    border-radius: 50%;
  }
  .card-front .edge-emblem {
    left: 420px;
    background: linear-gradient(160deg, var(--brand-blue-light), var(--brand-blue));
  }
  .card-back .edge-emblem {
    left: -137px;
    background: linear-gradient(160deg, var(--silver-light), var(--silver-dark));
  }

  .wordmark {
    position: absolute;
    margin: 0;
    font-family: "Work Sans", sans-serif;
    font-weight: 600;
    letter-spacing: -0.5px;
    color: var(--brand-blue);
    line-height: 1;
  }
  .card-front .wordmark {
    left: 31px;
    top: 34px;
    font-size: 34px;
  }
  .back-brand {
    position: absolute;
    right: 40px;
    top: 104px;
    width: 170px;
    display: flex;
    flex-direction: column;
    align-items: center;
    gap: 24px;
  }
  .back-brand .wordmark {
    position: static;
    font-size: 25px;
  }
  .brand-circle {
    width: 124px;
    height: 124px;
    border-radius: 50%;
    background: linear-gradient(90deg, var(--brand-blue) 0%, var(--brand-blue-light) 45%, var(--silver-dark) 100%);
  }

  .contact-block {
    position: absolute;
    left: 31px;
    top: 142px;
    font-family: "Work Sans", sans-serif;
    color: var(--ink);
  }
  .person-name {
    margin: 0;
    font-family: "Roboto", sans-serif;
    font-weight: 500;
    font-size: 21px;
    color: var(--brand-blue);
    line-height: 1.1;
  }
  .person-title {
    margin: 1px 0 0;
    font-size: 13.5px;
    line-height: 1.2;
  }
  .address {
    margin: 10px 0 0;
    font-size: 14px;
    line-height: 17px;
    font-style: normal;
  }
  .contact-list {
    list-style: none;
    margin: 9px 0 0;
    padding: 0;
    font-size: 14px;
    line-height: 17px;
  }
  .contact-list li {
    display: flex;
    align-items: center;
    gap: 6px;
  }
  .contact-icon {
    width: 9px;
    height: 9px;
    flex: none;
  }
</style>
</head>
<body>
<div class="canvas">

  <section class="card card-front" aria-label="Business card front">
    <div class="edge-emblem" role="img" aria-label="Large brand emblem in blue bleeding off the right edge"></div>
    <h1 class="wordmark">KESTRELGATE</h1>

    <div class="contact-block">
      <h2 class="person-name">Mitchell Parkhurst</h2>
      <p class="person-title">President &amp; CEO</p>
      <address class="address">
        4873 North 52nd Avenue, Ste 700<br>
        Omaha, NE 68142
      </address>
      <ul class="contact-list">
        <li>
          <svg class="contact-icon" viewBox="0 0 10 10" aria-hidden="true">
            <path d="M2 0.5 L3.6 0.5 L4.2 3 L3 3.8 Q4 6.2 6.2 7 L7 5.8 L9.5 6.4 L9.5 8 Q9.5 9.5 8 9.5 Q1 9 0.5 2 Q0.5 0.5 2 0.5 Z" fill="var(--brand-blue)"/>
          </svg>
          (402) 786-4259
        </li>
        <li>
          <svg class="contact-icon" viewBox="0 0 10 10" aria-hidden="true">
            <rect x="0.7" y="2" width="8.6" height="6" fill="none" stroke="var(--brand-blue)" stroke-width="1.2"/>
            <path d="M0.7 2 L5 5.5 L9.3 2" fill="none" stroke="var(--brand-blue)" stroke-width="1.2"/>
          </svg>
          mitchell@kestrelgateproperties.example
        </li>
        <li>
          <svg class="contact-icon" viewBox="0 0 10 10" aria-hidden="true">
            <circle cx="5" cy="5" r="4.3" fill="none" stroke="var(--brand-blue)" stroke-width="1"/>
            <ellipse cx="5" cy="5" rx="1.8" ry="4.3" fill="none" stroke="var(--brand-blue)" stroke-width="0.9"/>
            <line x1="0.7" y1="5" x2="9.3" y2="5" stroke="var(--brand-blue)" stroke-width="0.9"/>
          </svg>
          www.KestrelgateProperties.example
        </li>
      </ul>
    </div>
  </section>

  <section class="card card-back" aria-label="Business card back">
    <div class="edge-emblem" role="img" aria-label="Large brand emblem in silver bleeding off the left edge"></div>
    <div class="back-brand">
      <span class="brand-circle" role="img" aria-label="Brand emblem"></span>
      <p class="wordmark">KESTRELGATE</p>
    </div>
  </section>

</div>
</body>
</html>
```